Marcus Lindqvist Photography needs a business card designs

I am looking for a business card with a logo clean and simple which I can use that logo on my website or on my pictures. It has to be very classy and very professional. Please look at my website at www.marcuslvqphoto.com for my signature. I'm thinking of something like that for my signature/logo. I'm still working on my website but you get an idea. I'm open to any design but not too busy graphics.

I will be printing the business card from qrivel.com.

Surprise me :)

contact me if you have any questions.

-ML

I'm receiving a lot of black background at the moment. I know my website is all black doesn't mean I want my card to be all black. Please send in with some white background as well. Thanks :)

check out some business cards that I found online. I think they are simple and look really awesome. I don't want a card that is too busy.

http://www.marcuslvqphoto.com/p270092084

Reason: Please extend the date for me. I haven't really receive any good design yet.

Printing

• -a logo that related to my first and last initial of my name "ML"
-double sided
• -I don't want my background to be all black.
-no pictures on the card

```html
<!DOCTYPE html>
<html lang="en">
<head>
<meta charset="utf-8">
<title>Marcus Lindqvist Photography – Business Cards</title>
<link rel="stylesheet" href="https://fonts.googleapis.com/css2?family=Didact+Gothic&display=swap">
<style>
  :root {
    --canvas: #e8e5e1;
    --card-dark: #231f20;
    --accent-red: #ed1c24;
    --edge-white: #ffffff;
    --edge-grey: #5b5b5d;
    --ink-light: #ffffff;
    --card-w: 538px;
    --card-h: 308px;
  }
  * { box-sizing: border-box; margin: 0; padding: 0; }
  html, body {
    width: 1200px;
    height: 900px;
    overflow: hidden;
    background: var(--canvas);
    font-family: "Didact Gothic", "Century Gothic", sans-serif;
    color: var(--ink-light);
  }
  .card-sheet {
    position: relative;
    width: 1200px;
    height: 900px;
  }
  .card {
    position: absolute;
    width: var(--card-w);
    height: var(--card-h);
    overflow: hidden;
    box-shadow: 0 2px 6px rgba(0,0,0,0.18);
  }
  .card--front.card--white-edge { left: 40px;  top: 124px; }
  .card--back.card--white-edge  { left: 632px; top: 124px; }
  .card--front.card--grey-edge  { left: 40px;  top: 478px; }
  .card--back.card--grey-edge   { left: 632px; top: 478px; }

  .card__shapes {
    position: absolute;
    inset: 0;
    width: 100%;
    height: 100%;
  }
  .card--white-edge .shape-edge { fill: var(--edge-white); }
  .card--grey-edge .shape-edge  { fill: var(--edge-grey); }
  .shape-body { fill: var(--card-dark); }
  .shape-red  { fill: var(--accent-red); }

  .brand {
    position: absolute;
    display: flex;
    align-items: center;
    gap: 14px;
    color: var(--ink-light);
  }
  .brand__square {
    width: 40px;
    height: 40px;
    border: 2px solid var(--ink-light);
  }
  .brand__name {
    font-size: 22px;
    line-height: 1.05;
    letter-spacing: 0.5px;
  }
  .brand__name span { display: block; letter-spacing: 3px; }

  .card--front .brand { left: 78px; top: 28px; }
  .card--back .brand  { left: 50%; top: 124px; transform: translateX(-50%); }

  .contact {
    position: absolute;
    right: 47px;
    top: 196px;
    text-align: right;
  }
  .contact__name {
    font-size: 22px;
    letter-spacing: 2px;
    margin-bottom: 12px;
  }
  .contact__line {
    font-size: 15px;
    letter-spacing: 1.4px;
    line-height: 20px;
  }
  .contact__label { font-weight: bold; margin-right: 4px; }

  .website {
    position: absolute;
    left: 0;
    right: 0;
    top: 242px;
    text-align: center;
    font-size: 16px;
    letter-spacing: 2px;
  }
</style>
</head>
<body>
<main class="card-sheet">

  <section class="card card--front card--white-edge">
    <svg class="card__shapes" viewBox="0 0 448 257" preserveAspectRatio="none" aria-hidden="true">
      <rect class="shape-edge" width="448" height="257"/>
      <polygon class="shape-body" points="10,0 195,0 448,25 448,257 0,257 0,175"/>
      <polygon class="shape-red" points="0,233 432,257 0,257"/>
      <polygon class="shape-red" points="448,80 448,257 432,257"/>
    </svg>
    <div class="brand">
      <div class="brand__square"></div>
      <div class="brand__name">Marcus Lindqvist<span>Photography</span></div>
    </div>
    <div class="contact">
      <p class="contact__name">Marcus Lindqvist</p>
      <p class="contact__line"><span class="contact__label">P</span>415-555-0192</p>
      <p class="contact__line"><span class="contact__label">E</span>marcus@marcuslvqphoto.com</p>
    </div>
  </section>

  <section class="card card--back card--white-edge">
    <svg class="card__shapes" viewBox="0 0 448 257" preserveAspectRatio="none" aria-hidden="true">
      <rect class="shape-edge" width="448" height="257"/>
      <polygon class="shape-body" points="14,0 195,0 448,25 448,257 0,257 0,175"/>
      <polygon class="shape-red" points="0,233 432,257 0,257"/>
      <polygon class="shape-red" points="448,80 448,257 432,257"/>
    </svg>
    <div class="brand">
      <div class="brand__square"></div>
      <div class="brand__name">Marcus Lindqvist<span>Photography</span></div>
    </div>
    <p class="website">www.marcuslvqphoto.com</p>
  </section>

  <section class="card card--front card--grey-edge">
    <svg class="card__shapes" viewBox="0 0 448 257" preserveAspectRatio="none" aria-hidden="true">
      <rect class="shape-edge" width="448" height="257"/>
      <polygon class="shape-body" points="10,0 195,0 448,25 448,257 0,257 0,175"/>
      <polygon class="shape-red" points="0,233 432,257 0,257"/>
      <polygon class="shape-red" points="448,80 448,257 432,257"/>
    </svg>
    <div class="brand">
      <div class="brand__square"></div>
      <div class="brand__name">Marcus Lindqvist<span>Photography</span></div>
    </div>
    <div class="contact">
      <p class="contact__name">Marcus Lindqvist</p>
      <p class="contact__line"><span class="contact__label">P</span>415-555-0192</p>
      <p class="contact__line"><span class="contact__label">E</span>marcus@marcuslvqphoto.com</p>
    </div>
  </section>

  <section class="card card--back card--grey-edge">
    <svg class="card__shapes" viewBox="0 0 448 257" preserveAspectRatio="none" aria-hidden="true">
      <rect class="shape-edge" width="448" height="257"/>
      <polygon class="shape-body" points="14,0 195,0 448,25 448,257 0,257 0,175"/>
      <polygon class="shape-red" points="0,233 432,257 0,257"/>
      <polygon class="shape-red" points="448,80 448,257 432,257"/>
    </svg>
    <div class="brand">
      <div class="brand__square"></div>
      <div class="brand__name">Marcus Lindqvist<span>Photography</span></div>
    </div>
    <p class="website">www.marcuslvqphoto.com</p>
  </section>

</main>
</body>
</html>
```